Dental Design, very professional and noticable

Copperleaf Ridge Dental Surgery is based in Pelican Waters. We are a fast growing dental surgery and are looking for some professional business cards to send to patients.
We would like to see a design that is Vertical and uses the colours Soft Blue, Silver, White and Black. Maybe a full blue side with moto and details on back? Any other ideas or colours that you may think will make the card look unique is fine.
We need all details on the card that are listed above

Target Market(s)

Families, Retired, Other Professionals and Businesses

Industry/Entity Type

Dental

Contact Information for Business Card

Copperleaf Ridge Dental Surgery
Family, Cosmetic, Preventative
Dr. Owen Farrish
Dental Surgeon
BDS (Adel) FAE FADI FICD FPFA
phone: (07)54810296
fax: (07)54926170
email: copperleafridgedental@quillpost.net
http://copperleafridgedental.quillpost.net/

Logo Text

Logo styles of interest
Abstract Logo
Requirements
Must have
• Vertical, Vibrant but Professional, Rounded Edges, Logo on front and back of card (different colours on each side)
Nice to have
• One side completely blue (not sure what shade) with logo and moto on bottom
Other side white, with blue or different coloured logo with details in black and silver?
Logo should show half circle with 1 end as arrow symbolizing pelican waters canal also a magnifine glass also half circled with 1 end as arrow. Any other ideas are welcome.
Should not have
• A tooth. A smile. Toothbrush or Toothpaste. Cornered edges.

```html
<!DOCTYPE html>
<html lang="en">
<head>
<meta charset="utf-8">
<title>Copperleaf Ridge Dental Surgery – Business Card</title>
<link href="https://fonts.googleapis.com/css2?family=Open+Sans:wght@400&family=Philosopher:wght@700&display=swap" rel="stylesheet">
<style>
  :root {
    --stage: #141618;
    --soft-blue: #58e9f8;
    --icon-blue: #8fdcff;
    --icon-deep: #2b9fe0;
    --white: #ffffff;
    --gold: #98721a;
    --olive: #b1aa1c;
  }
  html, body {
    margin: 0;
    width: 1200px;
    height: 1000px;
    overflow: hidden;
    background: var(--stage);
  }
  .canvas { position: relative; width: 1200px; height: 1000px; }
  .card {
    position: absolute;
    top: 142px;
    width: 456px;
    height: 785px;
    border-radius: 32px;
    overflow: hidden;
    font-family: "Open Sans", Arial, sans-serif;
  }
  .card--front { left: 111px; background: var(--soft-blue); color: var(--white); }
  .card--back { left: 650px; width: 455px; background: var(--white); }
  .text-line { position: absolute; left: 0; right: 0; text-align: center; margin: 0; white-space: nowrap; }

  .brand-dot { position: absolute; border-radius: 50%; }
  .card--front .brand-dot { left: 182px; top: 495px; width: 80px; height: 80px; background: var(--white); }
  .card--front .brand-name { top: 609px; font-size: 29px; }
  .card--front .motto { top: 661px; font-size: 23px; left: -8px; }

  .card--back .brand-dot { left: 182px; top: 92px; width: 90px; height: 90px; background: var(--gold); }
  .card--back .brand-name { top: 205px; font-family: "Philosopher", Georgia, serif; font-weight: 700; font-size: 28px; color: var(--gold); }
  .card--back .motto { top: 258px; font-family: "Philosopher", Georgia, serif; font-weight: 700; font-size: 23px; color: var(--olive); }

  .detail-panel { position: absolute; left: 0; top: 0; }
  .doctor { color: var(--white); font-size: 23px; }
  .doctor--name { top: 428px; left: 10px; }
  .doctor--quals { top: 466px; left: 10px; }

  .contact-list { position: absolute; left: 28px; top: 524px; margin: 0; padding: 0; list-style: none; }
  .contact-item { position: absolute; left: 0; display: flex; align-items: center; gap: 14px; white-space: nowrap; color: var(--white); }
  .contact-item svg { flex: none; }
  .contact-item--email { top: 0; font-size: 16px; }
  .contact-item--web { top: 50px; font-size: 15px; }
  .contact-item--phone { top: 103px; font-size: 20px; }
  .contact-item--fax { top: 151px; font-size: 20px; }
</style>
</head>
<body>
<main class="canvas">

  <section class="card card--front" aria-label="Card front">
    <span class="brand-dot"></span>
    <p class="text-line brand-name">Copperleaf Ridge Dental Surgery</p>
    <p class="text-line motto">Family, Cosmetic, Preventive</p>
  </section>

  <section class="card card--back" aria-label="Card back">
    <span class="brand-dot"></span>
    <p class="text-line brand-name">Copperleaf Ridge Dental Surgery</p>
    <p class="text-line motto">Family, Cosmetic, Preventive</p>

    <svg class="detail-panel" width="455" height="785" viewBox="0 0 455 785" aria-hidden="true">
      <path d="M72,379 H446 V450 C446,660 250,770 10,770 V441 A62,62 0 0 0 72,379 Z" fill="var(--soft-blue)"/>
    </svg>

    <p class="text-line doctor doctor--name">Dr. Owen Farrish Dental Surgeon</p>
    <p class="text-line doctor doctor--quals">BDS (Adel) FAE FADI FICD FPFA</p>

    <ul class="contact-list">
      <li class="contact-item contact-item--email">
        <svg width="36" height="36" viewBox="0 0 36 36"><circle cx="18" cy="18" r="17" fill="var(--icon-blue)" stroke="var(--white)" stroke-width="1.5"/><rect x="10" y="12" width="16" height="12" rx="1" fill="none" stroke="var(--white)" stroke-width="2"/><path d="M10,12 L18,19 L26,12" fill="none" stroke="var(--white)" stroke-width="2"/></svg>
        <span>copperleafridgedental@quillpost.net</span>
      </li>
      <li class="contact-item contact-item--web">
        <svg width="36" height="36" viewBox="0 0 36 36"><circle cx="18" cy="18" r="17" fill="var(--icon-blue)" stroke="var(--white)" stroke-width="1.5"/><circle cx="12" cy="24" r="2" fill="var(--white)"/><path d="M11,17 A8,8 0 0 1 19,25 M11,11 A14,14 0 0 1 25,25" fill="none" stroke="var(--white)" stroke-width="2.2"/></svg>
        <span>http://copperleafridgedental.quillpost.net</span>
      </li>
      <li class="contact-item contact-item--phone">
        <svg width="36" height="36" viewBox="0 0 36 36"><circle cx="18" cy="18" r="17" fill="var(--icon-blue)" stroke="var(--white)" stroke-width="1.5"/><rect x="13" y="8" width="10" height="20" rx="2" fill="var(--white)"/><rect x="15" y="11" width="6" height="7" fill="var(--icon-deep)"/></svg>
        <span>(07)54810296</span>
      </li>
      <li class="contact-item contact-item--fax">
        <svg width="36" height="36" viewBox="0 0 36 36"><circle cx="18" cy="18" r="17" fill="var(--icon-blue)" stroke="var(--white)" stroke-width="1.5"/><rect x="13" y="9" width="10" height="6" fill="var(--white)"/><rect x="9" y="15" width="18" height="9" rx="2" fill="var(--white)"/><rect x="13" y="21" width="10" height="6" fill="var(--white)" stroke="var(--icon-deep)" stroke-width="1"/></svg>
        <span>(07)54926170</span>
      </li>
    </ul>
  </section>

</main>
</body>
</html>
```